Marrowfell Website Concept

We would like a one page website. Please refer to the attached files for more information.

Please reference file attachment version 1.1.

```html
<!DOCTYPE html>
<html lang="en">
<head>
<meta charset="utf-8">
<title>Marrowfell 360</title>
<link rel="stylesheet" href="https://fonts.googleapis.com/css2?family=Roboto+Condensed:ital,wght@0,400;0,700;1,400&family=Roboto:wght@400;500&display=swap">
<style>
:root{
  --navy:#2f3f86;
  --sky:#6cbce8;
  --link:#3a9fe0;
  --text:#777;
  --dark:#333;
  --footer:#3b3b3b;
  --rule:#e2e2e2;
}
*{box-sizing:border-box;margin:0;padding:0}
html,body{width:863px;height:1200px;overflow:hidden;background:#fff}
body{font-family:Arial,Helvetica,sans-serif;color:var(--text);position:relative}
.page{position:relative;width:863px;height:1200px}
.abs{position:absolute}
.nw{white-space:nowrap}

.brand{left:94px;top:25px;display:flex;align-items:center;gap:8px}
.brand-mark{width:28px;height:28px;border-radius:50%;background:#cfd3e6}
.brand-name{font-family:"Roboto Condensed",sans-serif;font-weight:400;font-size:20px;color:var(--navy)}

.nav a{position:absolute;top:29px;height:24px;line-height:24px;font-family:Arial,sans-serif;font-size:11.2px;color:#444;text-decoration:none;white-space:nowrap}
.nav a.active{left:298px;width:57px;text-align:center;background:var(--sky);color:#fff}

.hero{left:94px;top:82px;width:675px;height:298px;background:linear-gradient(180deg,#6b4a2a 0%,#c78c3e 35%,#5b3a1c 70%,#2a1a0e 100%)}
.hero-ctrl{left:111px;top:358px;display:flex;gap:2px}
.hero-ctrl span{width:16px;height:16px;background:#222;display:flex;align-items:center;justify-content:center}

.welcome{left:0;width:863px;top:403px;text-align:center;font-family:"Roboto Condensed",sans-serif;font-weight:700;font-size:19px;color:var(--navy)}
.intro{left:0;width:863px;top:437px;text-align:center;font-size:8px;line-height:19.5px;color:var(--text);white-space:nowrap}
.btn-contact{left:343px;top:529px;width:178px;height:33px;background:linear-gradient(#4a4a4a,#1f1f1f);color:#fff;font-family:"Roboto Condensed",sans-serif;font-weight:700;font-size:13px;line-height:33px;text-align:center;box-shadow:0 2px 2px rgba(0,0,0,.3)}

.h2{font-family:"Roboto Condensed",sans-serif;font-weight:700;font-size:17.5px;color:var(--navy)}
.offer-ctrl{left:744px;top:592px;display:flex;gap:9px}

.service{width:340px;height:90px}
.service .thumb{position:absolute;left:0;top:0;width:107px;height:81px}
.service h3{position:absolute;left:122px;top:0;width:215px;font-family:Roboto,sans-serif;font-weight:500;font-size:12.5px;line-height:17px;color:#3a3a3a}
.service p{position:absolute;left:123px;font-size:8px;line-height:16px;color:var(--text);white-space:nowrap}
.service p a{color:var(--link);text-decoration:none;font-size:9px}

.col-text{font-family:"Roboto Condensed",sans-serif;font-size:8.2px;line-height:15px;color:var(--text);white-space:nowrap}
.btn-more{left:94px;top:1045px;width:73px;height:25px;background:var(--sky);color:#fff;font-family:"Roboto Condensed",sans-serif;font-weight:700;font-size:8.5px;line-height:25px;text-align:center;border-radius:2px}
.quote{font-family:Georgia,serif;font-size:22px;color:#555;line-height:1}
.author{font-family:"Roboto Condensed",sans-serif;font-size:10.5px;color:var(--link)}
.posted{font-family:"Roboto Condensed",sans-serif;font-style:italic;font-size:7px;color:#555}

.news-item{left:558px;width:222px}
.date{position:absolute;left:0;top:0;width:24px;height:24px;background:#333;color:#fff;font-family:"Roboto Condensed",sans-serif;font-size:8.5px;line-height:10px;text-align:center;padding-top:2px}
.news-title{position:absolute;left:33px;top:-2px;font-family:"Roboto Condensed",sans-serif;font-size:9.5px;line-height:13.5px;color:var(--link);white-space:nowrap}
.news-body{position:absolute;left:0;top:34px;line-height:16px}

.rule{left:94px;width:675px;top:1105px;height:1px;background:var(--rule)}
.footer{left:0;top:1124px;width:863px;height:76px;background:var(--footer);color:#fff;font-size:8px}
.footer p{position:absolute;left:95px}
.social{position:absolute;left:649px;top:28px;display:flex;gap:5px}
.social span{width:20px;height:20px;border:1.5px solid #fff;border-radius:50%}
</style>
</head>
<body>
<div class="page">

  <div class="abs brand"><span class="brand-mark"></span><span class="brand-name">Marrowfell</span></div>

  <nav class="nav">
    <a class="active" href="#">HOME</a>
    <a href="#" style="left:373px">ABOUT US</a>
    <a href="#" style="left:455px">SERVICES</a>
    <a href="#" style="left:537px">NEWS</a>
    <a href="#" style="left:599px">TESTIMONIALS</a>
    <a href="#" style="left:704px">CONTACT US</a>
  </nav>

  <div class="abs hero" role="img" aria-label="Photo of business people silhouetted against an office window at sunset, with a tablet showing a business chart"></div>
  <div class="abs hero-ctrl">
    <span><svg width="8" height="8" viewBox="0 0 8 8"><path d="M5.5 1 2.5 4l3 3" stroke="#fff" stroke-width="1.4" fill="none"/></svg></span>
    <span><svg width="8" height="8" viewBox="0 0 8 8"><path d="M2.5 1l3 3-3 3" stroke="#fff" stroke-width="1.4" fill="none"/></svg></span>
  </div>

  <h1 class="abs welcome">WELCOME TO MARROWFELL 360</h1>
  <p class="abs intro">Marrowfell is a United States-based tier one security firm specializing in the protection of financial services professionals, executives and their families.&nbsp; We manage engage-<br>ments resulting from general and specific threats throughout the United States and abroad on behalf of our domestic clients.&nbsp; We deliver our services exclusively<br>through associates and contractors with United States special operations, secret service, CIA, or equivalent experience and training.&nbsp; We are one of only a<br>handful firms that offers scalable, tier one security services in every market in the United States.</p>
  <div class="abs btn-contact">CONTACT MARROWFELL</div>

  <h2 class="abs h2" style="left:94px;top:587px">SERVICE OFFERINGS</h2>
  <div class="abs offer-ctrl">
    <svg width="7" height="8" viewBox="0 0 7 8"><path d="M5 1 2 4l3 3" stroke="#bbb" stroke-width="1.2" fill="none"/></svg>
    <svg width="7" height="8" viewBox="0 0 7 8"><path d="M2 1l3 3-3 3" stroke="#bbb" stroke-width="1.2" fill="none"/></svg>
  </div>

  <div class="abs service" style="left:94px;top:630px">
    <div class="thumb" role="img" aria-label="Illustration of arrows pointing at an assessment sign" style="background:linear-gradient(135deg,#8a8f94,#d8dadc 50%,#6f7478)"></div>
    <h3>Threat Assessment</h3>
    <p style="top:20px">Marrowfell is a United States-based tier one security firm<br>specializing in the protection of financial services profes-<br>sionals, executives and their families.&nbsp; We manage<br>engagements resulting from general and specific threat<br>domestic clients......<a href="#">READ MORE</a></p>
  </div>

  <div class="abs service" style="left:445px;top:630px">
    <div class="thumb" role="img" aria-label="Photo of chess pieces on a chessboard" style="background:linear-gradient(180deg,#eef0f2,#a9adb1 55%,#2d2d2d)"></div>
    <h3>Threat Avoidance Plan &amp;<br>Dossier Creation</h3>
    <p style="top:32px">Marrowfell is a United States-based tier one security firm<br>specializing in the protection of financial services profes-<br>sionals, executives and their families.&nbsp; We manage<br>domestic clients......<a href="#">READ MORE</a></p>
  </div>

  <div class="abs service" style="left:94px;top:764px">
    <div class="thumb" role="img" aria-label="Photo of hands sheltering a piggy bank" style="background:linear-gradient(180deg,#3c4450,#c9b8a8 55%,#e9e6e2)"></div>
    <h3>Elite Executive Protection</h3>
    <p style="top:20px">Marrowfell is a United States-based tier one security firm<br>specializing in the protection of financial services profes-<br>sionals, executives and their families.&nbsp; We manage<br>engagements resulting from general and specific threat<br>domestic clients......<a href="#">READ MORE</a></p>
  </div>

  <div class="abs service" style="left:445px;top:764px">
    <div class="thumb" role="img" aria-label="Illustration of a hand holding a small city scene" style="background:linear-gradient(180deg,#4f9fd8,#cfe6f5 50%,#e8c9a9)"></div>
    <h3>Threat Avoidance Plan &amp;<br>Dossier Maintenance</h3>
    <p style="top:36px">Marrowfell is a United States-based tier one security firm<br>specializing in the protection of financial services profes-<br>sionals, executives and their families.&nbsp; We manage<br>domestic clients......<a href="#">READ MORE</a></p>
  </div>

  <h2 class="abs h2" style="left:95px;top:898px">ABOUT US</h2>
  <p class="abs col-text" style="left:95px;top:926px">Sed ut perspiciatis unde omnis iste natus error sit voluptatem<br>accusantium doloremque laudantium, totam rem aperiam, eaque et<br>quasi architecto beatae vitae dicta sunt explicabo.....</p>
  <p class="abs col-text" style="left:95px;top:982px">&nbsp;Nemo enim ipsam voluptatem quia voluptas sit aspernatur aut odit<br>aut fugit, sed quia consequuntur magni dolores eos qui ratione&nbsp; sed<br>quia consequuntur magni&nbsp; voluptatem sequi nesciunt....</p>
  <div class="abs btn-more">READ MORE</div>

  <h2 class="abs h2" style="left:329px;top:898px">TESTIMONIALS</h2>
  <span class="abs quote" style="left:323px;top:927px">&ldquo;</span>
  <p class="abs col-text" style="left:341px;top:932px;line-height:16.2px">Doloremque laudantium, totam rem aperiam, eaque ipsa<br>quae ab illo inventore veritatis et quasi architecto beatae<br>vitae dicta sunt explicabo. Nemo enim ipsam voluptatem<br>quia voluptas sit aspernatur aut odit aut fugit, sed quia<br>consequuntur magni dolores eos qui ratione voluptatem ,<br>dolore magnam aliquam quaerat.....</p>
  <span class="abs quote" style="left:460px;top:1020px">&rdquo;</span>
  <p class="abs author nw" style="left:341px;top:1041px">Dana Whitcombe</p>
  <p class="abs posted nw" style="left:341px;top:1058px">Posed on 25 June 2014</p>

  <h2 class="abs h2" style="left:558px;top:898px">LATEST NEWS</h2>
  <div class="abs news-item" style="top:936px;height:70px">
    <div class="date">24<br>Jun</div>
    <p class="news-title">Neque porro quisquam est qui dolorem ipsum<br>quia dolor sit amet, consectetur....</p>
    <p class="news-body col-text">Sed ut perspiciatis unde omnis iste natus&nbsp; voluptatem accusantium<br>doloremque laudantium.........</p>
  </div>
  <div class="abs" style="left:558px;top:1008px;width:220px;height:1px;background:var(--rule)"></div>
  <div class="abs news-item" style="top:1021px;height:70px">
    <div class="date">24<br>Jun</div>
    <p class="news-title">Neque porro quisquam est qui dolorem ipsum<br>quia dolor sit amet, consectetur....</p>
    <p class="news-body col-text">Sed ut perspiciatis unde omnis iste natus&nbsp; voluptatem accusantium<br>doloremque laudantium.........</p>
  </div>

  <div class="abs rule"></div>

  <footer class="abs footer">
    <p style="top:20px">References available upon request</p>
    <p style="top:46px">Copy Rights 2014.All rights reserved Marrowfell, LLC</p>
    <div class="social" aria-label="Social links"><span></span><span></span><span></span><span></span><span></span></div>
  </footer>

</div>
</body>
</html>
```